Clever & creative business card needed for a pediatric dentist.

We need a business card for a pediatric dentist that is building a brand-new pediatric dental practice. He is funny, outgoing, and sociable, and he hopes to give his business card to dentists and pediatricians so that he can give them information of where to refer infants, children, and teenagers that need high quality and attainable dental care.

The name of the dental practice is Copper Fern Pediatric Dentistry. Logo design .png / .pdf/ .jpg are provided to aid in the design.

The dentist's last name is Tolvan (which sounds like "burger", as in "hamburger” or “cheeseburger"). Since it is pediatric practice, kudos will be given to designs that implement a little joke into the design - but hopefully in a small or hidden way (such as putting something like a cheeseburger on the back of the card, or hiding it an an abstract way).

Thank you!

Please make a design that incorporates colors. It should be fun! Not too serious. It does not have to follow the color scheme of the logos.

```html
<!DOCTYPE html>
<html lang="en">
<head>
<meta charset="utf-8">
<title>Copper Fern Pediatric Dentistry – Business Card</title>
<link href="https://fonts.googleapis.com/css2?family=Montserrat:wght@500;700&display=swap" rel="stylesheet">
<style>
  :root {
    --page: #f7f7f7;
    --green: #359a5c;
    --green-text: #2e9150;
    --green-soft: #5aa872;
    --mint: #9fd5a8;
    --orange: #f2b24c;
    --bronze: #a87f3e;
    --white: #ffffff;
    --ink: #1d1d1d;
  }
  html, body {
    margin: 0;
    width: 800px;
    height: 1200px;
    overflow: hidden;
    background: var(--page);
    font-family: "Montserrat", sans-serif;
  }
  .sheet {
    position: relative;
    width: 800px;
    height: 1200px;
  }
  .card {
    position: absolute;
    left: 80px;
    width: 640px;
    height: 366px;
    box-shadow: 0 6px 14px rgba(0,0,0,0.18);
  }
  .card svg { display: block; width: 100%; height: 100%; }
  .card-front { top: 170px; }
  .card-back { top: 640px; }

  .name { font-weight: 700; font-size: 44px; fill: var(--green-text); }
  .role { font-weight: 500; font-size: 30px; letter-spacing: 2px; fill: var(--green-text); }
  .contact { font-weight: 500; font-size: 27px; fill: var(--ink); }
  .practice-front { font-weight: 700; font-size: 36px; fill: var(--green-text); }
  .practice-back { font-weight: 500; fill: var(--white); }
  .practice-back .big { font-size: 46px; }
  .practice-back .small { font-size: 17px; letter-spacing: 6px; }
</style>
</head>
<body>
<main class="sheet">

  <!-- Front of card -->
  <section class="card card-front">
    <svg viewBox="0 0 954 545" xmlns="http://www.w3.org/2000/svg">
      <rect class="front-base" width="954" height="545" fill="var(--green)"/>
      <g class="wave-bands">
        <path d="M440,-5 C410,60 360,95 290,95 C220,95 170,85 120,110 C75,135 60,180 60,230 C60,320 110,395 190,420 C270,445 340,420 390,450 C430,475 440,510 455,550 L960,550 L960,-5Z"
              fill="none" stroke="var(--orange)" stroke-width="80"/>
        <path d="M440,-5 C410,60 360,95 290,95 C220,95 170,85 120,110 C75,135 60,180 60,230 C60,320 110,395 190,420 C270,445 340,420 390,450 C430,475 440,510 455,550 L960,550 L960,-5Z"
              fill="none" stroke="var(--bronze)" stroke-width="44"/>
        <path d="M440,-5 C410,60 360,95 290,95 C220,95 170,85 120,110 C75,135 60,180 60,230 C60,320 110,395 190,420 C270,445 340,420 390,450 C430,475 440,510 455,550 L960,550 L960,-5Z"
              fill="var(--white)"/>
      </g>

      <g class="practice-mark">
        <circle cx="258" cy="225" r="58" fill="var(--mint)"/>
        <text class="practice-front" x="258" y="345" text-anchor="middle">Copper Fern</text>
      </g>

      <g class="identity">
        <text class="name" x="478" y="133">Your Name Here</text>
        <text class="role" x="478" y="172">Dentist</text>
      </g>

      <g class="contacts">
        <g class="contact-row phone">
          <rect x="480" y="238" width="38" height="40" rx="8" fill="var(--orange)"/>
          <rect x="491" y="245" width="16" height="26" rx="3" fill="none" stroke="var(--white)" stroke-width="3"/>
          <line x1="530" y1="236" x2="530" y2="280" stroke="var(--bronze)" stroke-width="2"/>
          <text class="contact" x="540" y="268">+000-1234-5678</text>
        </g>
        <g class="contact-row landline">
          <rect x="480" y="290" width="38" height="40" rx="8" fill="var(--orange)"/>
          <path d="M490,301 h12 l6,6 v14 h-18z" fill="none" stroke="var(--white)" stroke-width="3"/>
          <line x1="530" y1="288" x2="530" y2="332" stroke="var(--bronze)" stroke-width="2"/>
          <text class="contact" x="540" y="320">555-123-4567</text>
        </g>
        <g class="contact-row email">
          <rect x="480" y="342" width="38" height="40" rx="8" fill="var(--orange)"/>
          <rect x="488" y="352" width="22" height="18" rx="2" fill="none" stroke="var(--white)" stroke-width="3"/>
          <path d="M488,353 l11,9 l11,-9" fill="none" stroke="var(--white)" stroke-width="3"/>
          <line x1="530" y1="340" x2="530" y2="384" stroke="var(--bronze)" stroke-width="2"/>
          <text class="contact" x="540" y="372">youremail@email.com</text>
        </g>
        <g class="contact-row address">
          <rect x="480" y="394" width="38" height="40" rx="8" fill="var(--orange)"/>
          <path d="M499,427 C491,417 489,412 489,408 a10,10 0 0 1 20,0 C509,412 507,417 499,427z" fill="var(--white)"/>
          <circle cx="499" cy="408" r="3.5" fill="var(--orange)"/>
          <line x1="530" y1="392" x2="530" y2="456" stroke="var(--bronze)" stroke-width="2"/>
          <text class="contact" x="540" y="422">123 Main Street</text>
          <text class="contact" x="540" y="450">11th Floor, Some City</text>
        </g>
      </g>
    </svg>
  </section>

  <!-- Back of card -->
  <section class="card card-back">
    <svg viewBox="0 0 954 545" xmlns="http://www.w3.org/2000/svg">
      <rect class="back-base" width="954" height="545" fill="var(--green)"/>
      <path class="burger-art" role="img" aria-label="Playful faint hamburger illustration, a nod to the dentist's name"
            d="M0,0 H430 C500,40 545,140 545,260 V545 H0Z" fill="var(--green-soft)"/>
      <g class="practice-mark">
        <circle cx="743" cy="335" r="50" fill="var(--white)"/>
        <text class="practice-back" text-anchor="middle">
          <tspan class="big" x="743" y="455">Copper Fern</tspan>
          <tspan class="small" x="743" y="488">PEDIATRIC DENTISTRY</tspan>
        </text>
      </g>
    </svg>
  </section>

</main>
</body>
</html>
```